VALUE Book Cover Design for New Sales Book

We need a book cover designed for an upcoming book
Colors should be RED - BLACK - WHITE
A sample of our CURRENT BOOK cover (which we like) is attached
We need ideas for an "icon" or "meme" style design for the cover SIMILAR to the examples provided and attached
We need an "icon" that suggests VALUE-- we'd like the "icon" to be somewhat abstract vs using scales or anything "obvious"-- but the icon should still speak to and demonstrate what VALUE is.

Target Market(s)

Sales Directors and CEO's of large sales organizations and small businesses

Industry/Entity Type

Sales, Consulting,

Font styles to use
Sans Serif

Colors

Designer to choose colors to be used in the design.

Requirements
Must have
• Must be clean - contemporary and professional
Should not have
• should not have photos

```html
<!DOCTYPE html>
<html lang="en">
<head>
<meta charset="utf-8">
<title>Closing Worth — Book Cover</title>
<link rel="stylesheet" href="https://fonts.googleapis.com/css2?family=Lato:wght@300;400;900&display=swap">
<style>
  :root {
    --ink: #231f20;
    --accent: #ed1c24;
    --accent-soft: #f6a3a6;
    --paper: #fdfcfd;
    --backdrop: #f5f5f5;
  }
  html, body {
    margin: 0;
    width: 1200px;
    height: 848px;
    overflow: hidden;
    background: var(--backdrop);
  }
  .stage {
    position: relative;
    width: 1200px;
    height: 848px;
  }
  .book-cover {
    position: absolute;
    left: 269px;
    top: 24px;
    width: 662px;
    height: 800px;
    background: var(--paper);
    box-shadow: 0 1px 4px rgba(0,0,0,0.18);
  }
  .book-cover svg { display: block; }
  .title-heavy { font-family: "Lato", sans-serif; font-weight: 900; fill: var(--ink); }
  .subtitle { font-family: "Lato", sans-serif; font-weight: 300; fill: var(--ink); }
  .author { font-family: "Lato", sans-serif; font-weight: 400; fill: var(--ink); }
  .accent { fill: var(--accent); }
  .rule { fill: var(--ink); }
  .gem-mark { fill: var(--accent-soft); }
</style>
</head>
<body>
<main class="stage">
  <section class="book-cover">
    <svg width="662" height="800" viewBox="0 0 662 800">
      <g class="spine">
        <text class="title-heavy" font-size="38" transform="translate(40 26) rotate(90)" textLength="350" lengthAdjust="spacingAndGlyphs">CLOSINGWORTH</text>
        <rect class="gem-mark" x="42" y="384" width="32" height="30" role="img" aria-label="Small diamond icon"/>
        <rect class="rule" x="39" y="424" width="4" height="347"/>
        <rect class="rule" x="73" y="424" width="4" height="347"/>
        <text class="subtitle" font-size="19" transform="translate(49 428) rotate(90)" textLength="338" lengthAdjust="spacingAndGlyphs">Ways to Close <tspan class="accent">Bigger</tspan> Deals at <tspan class="accent">Better</tspan> Margins</text>
      </g>

      <g class="front-title">
        <text class="title-heavy" x="122" y="376" font-size="138" textLength="508" lengthAdjust="spacingAndGlyphs">CLOSING</text>
        <text class="title-heavy" x="122" y="476" font-size="138" textLength="400" lengthAdjust="spacingAndGlyphs">WORTH</text>
        <rect class="gem-mark" x="540" y="384" width="93" height="92" role="img" aria-label="Diamond icon outlined in red, symbol of value"/>
        <rect class="rule" x="122" y="491" width="511" height="5"/>
        <text class="subtitle" x="122" y="527" font-size="30" textLength="511" lengthAdjust="spacingAndGlyphs">Ways to Close <tspan class="accent">Bigger</tspan> Deals at <tspan class="accent">Better</tspan> Margins</text>
        <rect class="rule" x="122" y="537" width="511" height="5"/>
      </g>

      <text class="author" x="379" y="678" font-size="23" text-anchor="middle">Daniel Harrow, Ph.D</text>
    </svg>
  </section>
</main>
</body>
</html>
```